Yard Sign Design Needed

Yard sign needed for mowing & landscaping company. Would like to use the top logo with black background which is attached. Would like MOWING to be in large standout letters. The word "landscaping" can be smaller and more artistic or omitted. Will need room for phone number once design is approved. The phone number will need to stand out and look identical/similar to the word 'MOWING"

```html
<!DOCTYPE html>
<html lang="en">
<head>
<meta charset="utf-8">
<title>Brixley Contractors – Mowing Yard Sign</title>
<link rel="stylesheet" href="https://fonts.googleapis.com/css2?family=Montserrat:wght@400;600;700;800&family=Open+Sans:wght@400&display=swap">
<style>
  :root {
    --sign-green: #95ae12;
    --sign-black: #000000;
    --sign-white: #ffffff;
    --backdrop: #e8e3da;
  }
  html, body {
    margin: 0;
    padding: 0;
    width: 1200px;
    height: 720px;
    overflow: hidden;
    background: var(--backdrop);
  }
  .yard-sign {
    display: block;
    width: 1200px;
    height: 720px;
  }
  .sign-panel {
    fill: var(--sign-black);
    stroke: var(--sign-green);
    stroke-width: 18;
    stroke-linejoin: round;
  }
  .brand-mark { fill: var(--sign-green); }
  .brand-name {
    font-family: 'Montserrat', sans-serif;
    font-weight: 600;
    fill: var(--sign-green);
  }
  .headline {
    font-family: 'Montserrat', sans-serif;
    font-weight: 800;
    fill: var(--sign-green);
  }
  .subline {
    font-family: 'Montserrat', sans-serif;
    font-weight: 400;
    fill: var(--sign-white);
  }
  .phone-frame {
    fill: none;
    stroke: var(--sign-green);
    stroke-width: 4;
  }
  .phone-number {
    font-family: 'Montserrat', sans-serif;
    font-weight: 700;
    fill: var(--sign-green);
  }
  .web-gap { fill: var(--sign-black); }
  .web-address {
    font-family: 'Open Sans', sans-serif;
    font-weight: 400;
    fill: var(--sign-white);
  }
</style>
</head>
<body>
<svg class="yard-sign" viewBox="0 0 1200 720" xmlns="http://www.w3.org/2000/svg">
  <polygon class="sign-panel" points="585,37 1038,349 843,686 333,686 131,349"/>

  <g class="brand">
    <rect class="brand-mark" x="563" y="110" width="44" height="44"/>
    <text class="brand-name" x="585" y="218" font-size="34" text-anchor="middle" textLength="154" lengthAdjust="spacingAndGlyphs">BRIXLEY</text>
    <text class="brand-name" x="585" y="240" font-size="15" text-anchor="middle" textLength="156" lengthAdjust="spacing">CONTRACTORS LLC</text>
  </g>

  <text class="headline" x="266" y="416" font-size="142" textLength="641" lengthAdjust="spacingAndGlyphs">MOWING</text>

  <text class="subline" x="266" y="476" font-size="34" textLength="640" lengthAdjust="spacing">LANDSCAPING</text>

  <g class="contact">
    <rect class="phone-frame" x="365" y="524" width="440" height="106" rx="10"/>
    <rect class="web-gap" x="418" y="616" width="334" height="26"/>
    <text class="phone-number" x="382" y="593" font-size="60" textLength="405" lengthAdjust="spacingAndGlyphs">0 555 014 726</text>
    <text class="web-address" x="585" y="633" font-size="24" text-anchor="middle">www.brixleycontractors.com</text>
  </g>
</svg>
</body>
</html>
```